Imported Fine Wine E-commerce site

We need an e-commerce site built from scratch. We currently have a website however it is on Magento and would like a more user friendly platform. Not sure if its possible to use any of the information. We're looking for a mostly white clean design with some red to match the logo.

Target Market(s)

30+

Coding

Coded - Design and coding required

Number of Pages Required

5+ page

Colors
ec1f27

Requirements
Must have
• Categories 'Red/White/Bubbles/Mixed cases/Gifts/Wholesale'
'sort by' functions.
Contact us form
Filter by on left hand side, Variety, Price, Region
Mobile friendly
Must be on a platform that i can update and make changes to it myself

```html
<!DOCTYPE html>
<html lang="en">
<head>
<meta charset="utf-8">
<title>Cepa Fina – About Us</title>
<link href="https://fonts.googleapis.com/css2?family=Oswald:wght@400;500;600&family=Rubik:wght@500;700&family=Karla:wght@400;500&family=Roboto:wght@400;500&display=swap" rel="stylesheet">
<style>
:root{
  --wine:#6b0a1c;
  --red:#ec1f27;
  --dark:#1f1a1b;
  --ink:#222;
  --text:#333;
  --paper:#ececec;
  --white:#fff;
  --footer:#1b1b1b;
}
*{margin:0;padding:0;box-sizing:border-box}
html,body{width:1200px;height:2855px;overflow:hidden}
body{position:relative;background:var(--white);font-family:'Karla',sans-serif;color:var(--text)}
.abs{position:absolute}
/* top bar */
.topbar{left:0;top:0;width:1200px;height:33px;background:var(--dark);color:#fff;font:500 13px 'Roboto',sans-serif;letter-spacing:.3px}
.topbar span{position:absolute;top:9px;display:flex;align-items:center;gap:6px}
.social-dot{position:absolute;top:10px;width:12px;height:12px;border-radius:50%;border:1.5px solid #fff}
/* header */
.search{left:145px;top:62px;width:310px;height:45px;border:1px solid #ddd;background:#f3f3f3;font:13px 'Roboto',sans-serif;color:#555;padding:14px 20px}
.search svg{position:absolute;right:18px;top:15px}
.wholesale{left:831px;top:63px;width:151px;height:43px;border:2px solid var(--wine);color:var(--wine);font:500 15px 'Oswald',sans-serif;text-align:center;line-height:39px;letter-spacing:-.3px}
.cart{left:1013px;top:72px}
.nav{left:0;top:137px;width:1200px;height:53px;background:var(--wine)}
.nav a{position:absolute;top:15px;color:#fff;text-decoration:none;font:400 15px 'Oswald',sans-serif;letter-spacing:-.2px}
.nav a.active{text-decoration:underline;text-underline-offset:5px}
.brand-badge{left:511px;top:15px;width:200px;height:180px;border-radius:50%;background:#fff;display:flex;flex-direction:column;align-items:center;justify-content:center;z-index:2}
.brand-badge b{font:400 46px 'Oswald',sans-serif;color:var(--ink);line-height:1}
/* hero */
.hero{left:0;top:190px;width:1200px;height:331px;background:linear-gradient(100deg,#2f3a24 0%,#4c5a2f 45%,#3c2f3a 75%,#2a2233 100%)}
.hero h1{left:142px;top:88px;font:500 44px 'Oswald',sans-serif;color:#fff;letter-spacing:-.5px}
.hero .rule{left:142px;top:145px;width:300px;height:2px;background:var(--red)}
.hero p{left:142px;top:172px;width:385px;font:400 14.5px/19.5px 'Roboto',sans-serif;color:#fff}
/* about */
.about{left:0;top:521px;width:1200px;height:1143px;background:var(--paper)}
.photo{background:linear-gradient(160deg,#a59a58,#6b6a2e 55%,#3b3620)}
.photo.barrels{background:linear-gradient(170deg,#6d6a3a,#5a4632 55%,#7c5a44)}
.corner{position:absolute;border-color:var(--wine);border-style:solid}
.about h2{font:700 30px 'Rubik',sans-serif;color:var(--ink)}
.about p{font:400 14.5px/22.5px 'Karla',sans-serif;color:#333}
/* newsletter */
.news{left:0;top:1664px;width:661px;height:361px;background:linear-gradient(110deg,#3f4a2c,#56633a 45%,#3a3040 80%,#5b5232)}
.news h2{left:0;width:661px;top:82px;text-align:center;font:500 44px 'Oswald',sans-serif;color:#fff;letter-spacing:-.5px}
.news p{left:0;width:726px;top:147px;text-align:center;font:400 16px/24px 'Roboto',sans-serif;color:#fff}
.news .field{left:144px;top:214px;width:438px;height:40px;border-radius:20px;background:#fff;font:12px 'Roboto',sans-serif;color:#555;padding:13px 15px}
.news .btn{left:444px;top:214px;width:138px;height:40px;border-radius:20px;background:var(--wine);color:#fff;font:500 14px 'Roboto',sans-serif;text-align:center;line-height:40px}
.brand-panel{left:661px;top:1664px;width:539px;height:361px;background:#e6e6e6;display:flex;align-items:center;justify-content:center}
.brand-panel b{font:400 110px 'Oswald',sans-serif;color:var(--ink);letter-spacing:-2px}
/* partners */
.partners h2{left:0;width:1200px;top:2095px;text-align:center;font:700 38px 'Rubik',sans-serif;color:var(--ink)}
.partners .rule{left:560px;top:2165px;width:80px;height:3px;background:var(--red)}
.pbox{top:2216px;width:140px;height:81px;border:1px solid #ccc;background:#fff;display:flex;align-items:center;justify-content:center}
.pbox i{display:block;width:70px;height:26px;background:#ddd;border-radius:3px}
/* footer */
.footer{left:0;top:2392px;width:1200px;height:463px;background:var(--footer);color:#ddd}
.footer h3{font:500 18px 'Rubik',sans-serif;color:#fff;letter-spacing:.5px}
.footer ul{list-style:none;font:400 14.5px/26.5px 'Roboto',sans-serif;color:#ccc}
.f-brand{font:400 52px 'Oswald',sans-serif;color:#fff}
.f-social{width:34px;height:34px;border-radius:50%;border:1.5px solid #fff}
.footer .divider{left:140px;top:346px;width:940px;height:1px;background:#3a3a3a}
.footer .copy{left:0;width:1200px;top:390px;text-align:center;font:400 15.5px 'Roboto',sans-serif;color:#ddd}
</style>
</head>
<body>

<div class="abs topbar">
  <span style="left:145px"><svg width="12" height="12" viewBox="0 0 24 24"><path fill="#fff" d="M6.6 10.8a15 15 0 0 0 6.6 6.6l2.2-2.2c.3-.3.7-.4 1-.2 1.1.4 2.3.6 3.6.6.6 0 1 .4 1 1V20c0 .6-.4 1-1 1A17 17 0 0 1 3 4c0-.6.4-1 1-1h3.5c.6 0 1 .4 1 1 0 1.3.2 2.5.6 3.6.1.3 0 .7-.2 1z"/></svg>TOLL FREE : 1300 555 019</span>
  <span style="left:369px"><svg width="12" height="12" viewBox="0 0 24 24"><circle cx="12" cy="12" r="9.5" fill="none" stroke="#fff" stroke-width="2.5"/><path d="M12 6v6l4 2" stroke="#fff" stroke-width="2.5" fill="none"/></svg>8AM-5PM MON-FRI</span>
  <span style="left:737px">CORPORATE ACCOUNTS &nbsp;&nbsp;|&nbsp;&nbsp; LOGIN</span>
  <i class="social-dot" style="left:1003px"></i><i class="social-dot" style="left:1022px"></i><i class="social-dot" style="left:1041px"></i>
</div>

<div class="abs search">Search products...<svg width="13" height="13" viewBox="0 0 24 24"><circle cx="10" cy="10" r="7" fill="none" stroke="#444" stroke-width="3"/><path d="M15 15l6 6" stroke="#444" stroke-width="3"/></svg></div>
<div class="abs wholesale">WHOLESALE</div>
<svg class="abs cart" width="40" height="36" viewBox="0 0 40 36"><path d="M2 4h6l5 20h19l4-14H11" fill="none" stroke="#c0162a" stroke-width="2.5"/><circle cx="15" cy="30" r="2.5" fill="#c0162a"/><circle cx="29" cy="30" r="2.5" fill="#c0162a"/><circle cx="34" cy="4" r="6" fill="#fff" stroke="#555"/><text x="34" y="7.5" font-size="9" text-anchor="middle" fill="#333" font-family="Roboto,sans-serif">0</text></svg>

<nav class="abs nav">
  <a class="active" style="left:176px">HOME</a><a style="left:240px">WINES</a><a style="left:308px">BEER</a><a style="left:367px">SPIRITS</a><a style="left:443px">SPECIALS</a>
  <a style="left:722px">GIFT PACKS</a><a style="left:817px">ABOUT US</a><a style="left:905px">WINE CLUB</a><a style="left:997px">CONTACT</a>
</nav>
<div class="abs brand-badge"><b>Cepa Fina</b></div>

<section class="abs hero" role="img" aria-label="Vineyard with ripe dark grape clusters">
  <h1 class="abs">CEPA FINA ABOUT US</h1>
  <div class="abs rule"></div>
  <p class="abs">Sed ut perspiciatis unde omnis iste natus error sit voluptatem accusantium doloremque laudantium, totam rem aperiam, eaque ipsa quae ab illo inventore veritatis et quasi architecto beatae vitae dicta sunt explicabo.</p>
</section>

<section class="abs about">
  <div class="corner" style="left:145px;top:97px;width:62px;height:62px;border-width:4px 0 0 4px"></div>
  <div class="corner" style="left:540px;top:442px;width:62px;height:62px;border-width:0 4px 4px 0"></div>
  <div class="abs photo" style="left:149px;top:102px;width:448px;height:401px" role="img" aria-label="Wine bottle and glass on a barrel above vineyard at sunset"></div>
  <h2 class="abs" style="left:656px;top:122px">ABOUT US</h2>
  <p class="abs" style="left:655px;top:181px;width:405px">Cepa Fina was created with a simple but powerful vision........to deliver the best of South American wines directly to your door. We have an excellent array of wines particularly from the established wine growing regions of Chile, Argentina and Spain. We enjoy our wines and believe that once you try them you will also become passionate about their unique flavours.</p>
  <p class="abs" style="left:655px;top:349px;width:405px">Our wines and products are chosen with the greatest care and only the brands that are well renown for their quality and strong reputation are included in the site. Many have won international awards and developed a following outside of South America, particularly within the United States and United Kingdom.</p>

  <p class="abs" style="left:145px;top:662px;width:410px">Our team consists of qualified experts, including oenologists who can guide our customers to a selection of wines to suit their lifestyle whether it be entertaining, wine tasting or enjoying the sheer pleasure of an excellent wine with friends. We can also guide you in selecting wines to accompany that special dish you might like to prepare.</p>
  <p class="abs" style="left:145px;top:814px;width:410px">Whether you are a connoisseur of good wine or enjoy introduc­ing your palete to unique tantalizing flavours, we invite you to try our wines and enjoy the experience of ordering from Cepa Fina. If you have any questions, please contact us on  today and our friendly staff will be happy to assist you.</p>
  <div class="corner" style="left:601px;top:593px;width:62px;height:62px;border-width:4px 0 0 4px"></div>
  <div class="corner" style="left:997px;top:937px;width:62px;height:62px;border-width:0 4px 4px 0"></div>
  <div class="abs photo barrels" style="left:605px;top:597px;width:449px;height:402px" role="img" aria-label="Stacked oak wine barrels under a vine pergola"></div>
</section>

<section class="abs news" role="img" aria-label="Vineyard rows with grape clusters">
  <h2 class="abs">JOIN OUR NEWSLETTER</h2>
  <p class="abs" style="width:661px">Subscribe to our mailing list to receive updates<br>and promotional offers.</p>
  <div class="abs field">Enter your E - mail</div>
  <div class="abs btn">SUBSCRIBE</div>
</section>
<div class="abs brand-panel"><b>Cepa Fina</b></div>

<section class="partners">
  <h2 class="abs">OUR PARTNERS</h2>
  <div class="abs rule"></div>
  <svg class="abs" style="left:110px;top:2245px" width="14" height="20" viewBox="0 0 14 20"><path d="M11 2L3 10l8 8" fill="none" stroke="#333" stroke-width="2.5"/></svg>
  <div class="abs pbox" style="left:143px"><i></i></div>
  <div class="abs pbox" style="left:298px"><i></i></div>
  <div class="abs pbox" style="left:453px"><i></i></div>
  <div class="abs pbox" style="left:608px"><i></i></div>
  <div class="abs pbox" style="left:763px"><i></i></div>
  <div class="abs pbox" style="left:918px"><i></i></div>
  <svg class="abs" style="left:1074px;top:2245px" width="14" height="20" viewBox="0 0 14 20"><path d="M3 2l8 8-8 8" fill="none" stroke="#333" stroke-width="2.5"/></svg>
</section>

<footer class="abs footer">
  <div class="abs f-brand" style="left:160px;top:108px">Cepa Fina</div>
  <div class="abs f-social" style="left:175px;top:243px"></div>
  <div class="abs f-social" style="left:215px;top:243px"></div>
  <div class="abs f-social" style="left:255px;top:243px"></div>

  <div class="abs" style="left:422px;top:72px"><h3>QUICK LINKS</h3>
    <ul style="margin-top:12px"><li>Home</li><li>Wines</li><li>Beer</li><li>Spirits</li><li>Specials</li><li>About Us</li><li>Wine Club</li></ul></div>
  <div class="abs" style="left:616px;top:72px"><h3>INFORMATION</h3>
    <ul style="margin-top:12px"><li>Wholesale</li><li>Gift Packs</li><li>Corporate Accounts</li><li>Contact Us</li><li>International Shipping Info</li><li>Privacy &amp; Security</li><li>Satisfaction Guarantee</li></ul></div>
  <div class="abs" style="left:847px;top:72px"><h3>CONACT US</h3>
    <ul style="margin-top:14px;font-size:16px;line-height:32px;color:#eee">
      <li><svg width="16" height="16" viewBox="0 0 24 24" style="vertical-align:-2px;margin-right:12px"><path fill="#ec1f27" d="M6.6 10.8a15 15 0 0 0 6.6 6.6l2.2-2.2c.3-.3.7-.4 1-.2 1.1.4 2.3.6 3.6.6.6 0 1 .4 1 1V20c0 .6-.4 1-1 1A17 17 0 0 1 3 4c0-.6.4-1 1-1h3.5c.6 0 1 .4 1 1 0 1.3.2 2.5.6 3.6.1.3 0 .7-.2 1z"/></svg>1300 555 019</li>
      <li><svg width="18" height="13" viewBox="0 0 18 13" style="vertical-align:-1px;margin-right:13px"><rect width="18" height="13" fill="#ec1f27"/><path d="M0 0l9 7 9-7" fill="none" stroke="#1b1b1b" stroke-width="1.5"/></svg>info@CepaFina.com</li>
      <li style="padding-left:33px;font-size:14px">8am-5pm Mon-Fri CST</li>
    </ul></div>

  <div class="abs divider"></div>
  <div class="abs copy">© 2020 CepaFina | All Rights Reserved | Disclaimer</div>
</footer>

</body>
</html>
```